Marlow Crest Group (Real Estate and Investment)

A high end, clean design.
We are a real estate company with sales, asset management and investment divisions. We want to use a black and white scheme which is really high end feel. The back of the card can just be the logo (black background with the white writing) as we will probably emboss this when we print)

Target Market(s)

High level investors, high end houses for sale

Industry/Entity Type

Business

Contact Information for Business Card

Name, position, phone number and email address
Glen Varley, Managing Director, 0437259064 and glen@marlowcrest-example.com.au

Requirements
Must have
• Back of the card to be the black background with the white writing (as per the attached images). Would like the capacity to emboss the writing and logo

```html
<!DOCTYPE html>
<html lang="en">
<head>
<meta charset="utf-8">
<title>Marlow Crest Group – Business Card</title>
<link rel="stylesheet" href="https://fonts.googleapis.com/css2?family=Montserrat:wght@300;400&family=Roboto+Slab:wght@400&display=swap">
<style>
  :root {
    --canvas-bg: #e9e8e6;
    --card-black: #0b0b0b;
    --card-black-sheen: #3a3a3a;
    --card-white: #ffffff;
    --ink: #1a1a1a;
    --ink-soft: #4a4a4a;
    --ink-muted: #7a7a7a;
    --logo-white: #f4f4f4;
    --skyline-grey: #9d9d9d;
    --icon-bg: #2a2a2a;
  }
  * { box-sizing: border-box; margin: 0; padding: 0; }
  html, body {
    width: 1200px;
    height: 804px;
    overflow: hidden;
    background: var(--canvas-bg);
  }
  .canvas {
    position: relative;
    width: 1200px;
    height: 804px;
  }
  .card {
    position: absolute;
    top: 252px;
    width: 520px;
    height: 300px;
    border-radius: 18px;
    overflow: hidden;
    box-shadow: 0 10px 28px rgba(0,0,0,0.18);
  }

  /* Back of card */
  .card-back {
    left: 60px;
    background:
      linear-gradient(150deg, var(--card-black) 0%, var(--card-black) 45%, var(--card-black-sheen) 72%, var(--card-black) 100%);
  }
  .brand {
    position: absolute;
    left: 0; right: 0;
    top: 122px;
    display: flex;
    align-items: center;
    justify-content: center;
    gap: 16px;
  }
  .brand-dot {
    width: 34px;
    height: 34px;
    border-radius: 50%;
    border: 2px solid var(--logo-white);
  }
  .brand-name {
    font-family: "Montserrat", sans-serif;
    font-weight: 300;
    font-size: 30px;
    letter-spacing: 1px;
    color: var(--logo-white);
    text-transform: uppercase;
  }

  /* Front of card */
  .card-front {
    left: 620px;
    background: var(--card-white);
  }
  .person {
    position: absolute;
    left: 240px;
    top: 52px;
  }
  .person-name {
    font-family: "Roboto Slab", serif;
    font-weight: 400;
    font-size: 30px;
    color: var(--ink);
    line-height: 1;
  }
  .person-title {
    margin-top: 9px;
    margin-left: 18px;
    font-family: "Montserrat", sans-serif;
    font-weight: 400;
    font-size: 10px;
    color: var(--ink-muted);
  }
  .accent-bar {
    position: absolute;
    left: 0;
    top: 126px;
    width: 118px;
    height: 24px;
    background: linear-gradient(90deg, #000 0%, #000 60%, #6a6a6a 100%);
    border-radius: 0 4px 4px 0;
  }
  .contact {
    position: absolute;
    left: 96px;
    top: 154px;
    display: grid;
    grid-template-columns: 22px auto;
    column-gap: 12px;
    row-gap: 8px;
    align-items: center;
  }
  .contact-icon {
    width: 22px;
    height: 22px;
    border-radius: 5px;
    background: var(--icon-bg);
    display: flex;
    align-items: center;
    justify-content: center;
  }
  .contact-phone {
    font-family: "Montserrat", sans-serif;
    font-weight: 300;
    font-size: 21px;
    letter-spacing: 1px;
    color: var(--ink-soft);
  }
  .contact-email {
    font-family: "Montserrat", sans-serif;
    font-weight: 400;
    font-size: 10px;
    color: var(--ink-soft);
  }
  .skyline {
    position: absolute;
    left: 250px;
    right: 0;
    bottom: 0;
    height: 190px;
    background: linear-gradient(180deg, rgba(157,157,157,0) 0%, rgba(157,157,157,0.45) 40%, rgba(157,157,157,0.75) 100%);
    clip-path: polygon(0 100%, 0 80%, 12% 70%, 22% 55%, 35% 40%, 48% 30%, 60% 22%, 74% 12%, 88% 6%, 100% 0, 100% 100%);
  }
</style>
</head>
<body>
  <main class="canvas">
    <section class="card card-back" aria-label="Card back">
      <div class="brand">
        <span class="brand-dot"></span>
        <span class="brand-name">Marlow Crest Group</span>
      </div>
    </section>

    <section class="card card-front" aria-label="Card front">
      <div class="person">
        <p class="person-name">Glen Varley</p>
        <p class="person-title">Managing Director</p>
      </div>

      <div class="accent-bar"></div>

      <div class="contact">
        <span class="contact-icon">
          <svg width="12" height="12" viewBox="0 0 24 24" aria-hidden="true">
            <path fill="#fff" d="M6.6 10.8a15.1 15.1 0 0 0 6.6 6.6l2.2-2.2a1 1 0 0 1 1-.25 11.4 11.4 0 0 0 3.6.57 1 1 0 0 1 1 1V20a1 1 0 0 1-1 1A17 17 0 0 1 3 4a1 1 0 0 1 1-1h3.5a1 1 0 0 1 1 1c0 1.25.2 2.45.57 3.57a1 1 0 0 1-.25 1z"/>
          </svg>
        </span>
        <span class="contact-phone">0437259064</span>
        <span class="contact-icon">
          <svg width="12" height="12" viewBox="0 0 24 24" aria-hidden="true">
            <rect x="2" y="5" width="20" height="14" rx="1.5" fill="none" stroke="#fff" stroke-width="2"/>
            <path d="M2.5 6l9.5 7 9.5-7" fill="none" stroke="#fff" stroke-width="2"/>
          </svg>
        </span>
        <span class="contact-email">glen@marlowcrest-example.com.au</span>
      </div>

      <div class="skyline" role="img" aria-label="Sketched grey city skyline rising toward the right edge"></div>
    </section>
  </main>
</body>
</html>
```